Vel Techniqos Logo Design

We need a business card design for Las Vegas based company called "Vel Techniqs" (http://www.veltechniqs-example.com). Vel Techniqs prides itself in providing in-depth knowledge that is based on real-world experience in the field of wireless telecommunications. Our practice covers strategy, marketing, and business development across the entire telecom value chain – from consumer to enterprise, content to applications, and mobile devices to wireless infrastructure. Our expertise is in the fields of wireless telecommunications, network optimization, specializing in CDMA, UMTS, WiMAX and LTE solutions.
The logo attached could be reused for the business card, but would prefer a new innovative logo as well. The final design should project cutting edge wireless technologies. The design should also communicate a modern business that has expertise and is focused on R&D.
Updates

Team,

  Forgot to mention this.  While Vel Techniqs is focused in wireless technologies, the word 'Vel' comes from Hindi language and means harmonious music

Project Deadline Extended
Reason: Extending deadline to allow for the designer to complete final changes. Thank you all for submitting the designs so far. Thanks, Rohan.

Industry/Entity Type

Business

Logo Text

Vel Techniqs

```html
<!DOCTYPE html>
<html lang="en">
<head>
<meta charset="utf-8">
<title>Vel Techniqs – Business Card</title>
<link rel="stylesheet" href="https://fonts.googleapis.com/css2?family=Michroma&display=swap">
<style>
  :root {
    --stage: #3a3a3c;
    --card-white: #ffffff;
    --accent-blue: #1ca3e3;
    --ink-navy: #1b2b42;
    --logo-grey: #5d6670;
    --band-deep: #15518c;
    --band-mid: #1d6fb3;
    --band-light: #3a95d6;
    --text-on-band: #ffffff;
    --back-black: #000000;
    --back-mark: #c9ced5;
  }
  * { box-sizing: border-box; margin: 0; padding: 0; }
  html, body {
    width: 1006px;
    height: 1200px;
    overflow: hidden;
    background: var(--stage);
  }
  .canvas {
    position: relative;
    width: 1006px;
    height: 1200px;
    font-family: "Michroma", sans-serif;
  }
  .card {
    position: absolute;
    left: 88px;
    width: 838px;
    height: 490px;
    overflow: hidden;
  }
  .card--front { top: 83px; background: var(--card-white); }
  .card--back  { top: 629px; background: var(--back-black); }

  /* front: logo */
  .brand-dot {
    position: absolute;
    left: 140px;
    top: 71px;
    width: 138px;
    height: 138px;
    border-radius: 50%;
    background: var(--accent-blue);
  }
  .brand-name {
    position: absolute;
    left: 44px;
    top: 236px;
    font-size: 25px;
    letter-spacing: 1px;
    color: var(--logo-grey);
    white-space: nowrap;
  }

  /* front: faint decoration */
  .deco-circle {
    position: absolute;
    left: 621px;
    top: 248px;
    width: 246px;
    height: 246px;
    border-radius: 50%;
    background: radial-gradient(circle at 40% 35%, rgba(255,255,255,0.35), rgba(200,220,240,0.18) 60%, rgba(255,255,255,0.08));
    z-index: 2;
  }

  /* front: identity */
  .identity {
    position: absolute;
    right: 38px;
    top: 74px;
    text-align: right;
    z-index: 3;
  }
  .identity__name {
    font-size: 27px;
    letter-spacing: 4px;
    color: var(--accent-blue);
    line-height: 1;
  }
  .identity__title {
    margin-top: 12px;
    font-size: 15px;
    letter-spacing: 2.5px;
    color: var(--ink-navy);
  }
  .identity__address {
    margin-top: 38px;
    font-size: 17px;
    letter-spacing: 2px;
    line-height: 32px;
    color: var(--ink-navy);
    font-variant: small-caps;
  }

  /* front: contact band */
  .contact-band {
    position: absolute;
    left: 0;
    top: 322px;
    width: 100%;
    height: 168px;
    background: linear-gradient(90deg, var(--band-deep) 0%, var(--band-mid) 55%, var(--band-light) 100%);
  }
  .contact-list {
    position: absolute;
    left: 52px;
    top: 24px;
    list-style: none;
    color: var(--text-on-band);
    font-size: 16px;
    letter-spacing: 2px;
    line-height: 32px;
    font-variant: small-caps;
    white-space: nowrap;
    z-index: 3;
  }
  .contact-list__label { margin-right: 14px; }

  /* back */
  .back-mark {
    position: absolute;
    left: 0;
    top: 0;
    width: 100%;
    height: 100%;
    display: flex;
    flex-direction: column;
    align-items: center;
    justify-content: center;
    gap: 28px;
  }
  .back-mark__dot {
    width: 194px;
    height: 194px;
    border-radius: 50%;
    background: var(--accent-blue);
  }
  .back-mark__name {
    font-size: 22px;
    letter-spacing: 2px;
    color: var(--back-mark);
  }
</style>
</head>
<body>
<main class="canvas">
  <section class="card card--front" aria-label="Business card front">
    <div class="brand-dot" aria-hidden="true"></div>
    <div class="brand-name">VEL TECHNIQS</div>

    <div class="identity">
      <div class="identity__name">MARCUS HALE</div>
      <div class="identity__title">SUPERINTENDENT</div>
      <div class="identity__address">PO Box 417<br>Riverton</div>
    </div>

    <div class="contact-band">
      <ul class="contact-list">
        <li><span class="contact-list__label">Mobile:</span>(555) 014-2237</li>
        <li><span class="contact-list__label">Email:</span>marcus@veltechniqs-example.com</li>
        <li><span class="contact-list__label">Website:</span>www.veltechniqs-example.com</li>
      </ul>
    </div>

    <div class="deco-circle" aria-hidden="true"></div>
  </section>

  <section class="card card--back" aria-label="Business card back">
    <div class="back-mark">
      <div class="back-mark__dot" aria-hidden="true"></div>
      <div class="back-mark__name">VEL TECHNIQS</div>
    </div>
  </section>
</main>
</body>
</html>
```